Buisness card

**Front Side:**

**[Your Company Logo]**
**Steadfast Upkeep Engineering**
*Keeping Your Equipment Running Smoothly*

**Contact Information:**
- **Name:** [dale Harwick
- **Title:** [owner
- **Phone:** [5073918246
- **Email:** dale@suevx.com

**Back Side:**

**Services Offered:**
- Routine Inspections
- Equipment Maintenance
- Emergency Repairs
- Consultation Services
- New installs
Tag line
Be proactive not reactive

```html
<!DOCTYPE html>
<html lang="en">
<head>
<meta charset="utf-8">
<title>Steadfast Upkeep Engineering – Business Card</title>
<link rel="stylesheet" href="https://fonts.googleapis.com/css2?family=Lato:wght@400;700;900&family=Montserrat:wght@700;800&display=swap">
<style>
  :root {
    --bg: #1e1e1e;
    --card: #ffffff;
    --navy: #0f2a6e;
    --navy-deep: #062b6f;
    --blue: #0a74f5;
    --sky: #27c4f5;
    --ink: #2b2b2b;
    --rule: #3456a6;
  }
  * { box-sizing: border-box; margin: 0; padding: 0; }
  html, body { width: 1200px; height: 875px; overflow: hidden; }
  body {
    background: var(--bg);
    font-family: "Lato", sans-serif;
    position: relative;
  }
  .card {
    position: absolute;
    left: 280px;
    width: 640px;
    height: 366px;
    background: var(--card);
    border-radius: 22px;
    overflow: hidden;
  }
  .card--back { top: 48px; }
  .card--front { top: 461px; }

  /* Back */
  .back-wave { position: absolute; left: 0; bottom: 0; width: 640px; height: 366px; }
  .back-mark {
    position: absolute; left: 48px; top: 70px; width: 190px;
    display: flex; flex-direction: column; align-items: center; gap: 14px;
  }
  .back-mark__dot { width: 110px; height: 110px; border-radius: 50%; background: var(--navy); }
  .back-mark__name {
    font-family: "Montserrat", sans-serif; font-weight: 800; color: var(--navy);
    font-size: 17px; line-height: 1.2; text-align: center; text-transform: uppercase;
  }
  .back-divider {
    position: absolute; left: 268px; top: 56px; width: 1px; height: 150px; background: var(--rule);
  }
  .services { position: absolute; left: 300px; top: 56px; }
  .services__title {
    font-family: "Montserrat", sans-serif; font-weight: 800; color: var(--navy);
    font-size: 22px; letter-spacing: .5px; margin-bottom: 6px;
  }
  .services__list { list-style: none; }
  .services__list li {
    font-size: 17px; color: var(--ink); line-height: 1.35; padding-left: 18px; position: relative;
  }
  .services__list li::before {
    content: ""; position: absolute; left: 2px; top: 9px; width: 6px; height: 6px;
    border-radius: 50%; background: var(--blue);
  }
  .slogan {
    position: absolute; right: 40px; bottom: 58px;
    font-family: "Montserrat", sans-serif; font-weight: 700; color: #fff;
    font-size: 18px; letter-spacing: 1.5px; transform: rotate(-9deg); transform-origin: right bottom;
  }

  /* Front */
  .front-band { position: absolute; left: 0; top: 0; width: 150px; height: 366px; background: var(--navy-deep); }
  .front-disc {
    position: absolute; left: 36px; top: 64px; width: 170px; height: 170px; border-radius: 50%;
    background: #fff;
  }
  .brand { position: absolute; left: 236px; top: 40px; }
  .brand__name {
    font-family: "Montserrat", sans-serif; font-weight: 800; color: var(--navy);
    font-size: 30px; line-height: 1.05; text-transform: uppercase;
  }
  .brand__tag {
    font-family: "Montserrat", sans-serif; font-weight: 700; color: #111;
    font-size: 10.5px; letter-spacing: 1px; text-transform: uppercase; margin-top: 8px;
  }
  .person { position: absolute; left: 236px; top: 168px; }
  .person__name {
    font-family: "Montserrat", sans-serif; font-weight: 800; color: var(--navy);
    font-size: 30px; text-transform: uppercase; letter-spacing: .5px;
  }
  .person__title { color: var(--blue); font-size: 18px; margin-top: 2px; }
  .contacts { position: absolute; left: 236px; top: 250px; list-style: none; }
  .contacts li {
    display: flex; align-items: center; gap: 10px; font-size: 16px; color: var(--ink); line-height: 1.6;
  }
  .contacts svg { width: 14px; height: 14px; fill: var(--blue); flex: none; }
</style>
</head>
<body>

<section class="card card--back" aria-label="Card back">
  <svg class="back-wave" viewBox="0 0 640 366" aria-hidden="true">
    <path d="M0 320 C120 290 200 360 330 300 C440 250 520 180 640 175 L640 366 L0 366 Z" fill="var(--blue)"/>
  </svg>
  <div class="back-mark">
    <div class="back-mark__dot"></div>
    <div class="back-mark__name">Steadfast Upkeep Engineering</div>
  </div>
  <div class="back-divider"></div>
  <div class="services">
    <h2 class="services__title">SERVICES OFFERED:</h2>
    <ul class="services__list">
      <li>Routine Inspections</li>
      <li>Equipment Maintenance</li>
      <li>Emergency Repairs</li>
      <li>Consultation Services</li>
      <li>New installs</li>
    </ul>
  </div>
  <p class="slogan">BE PROACTIVE NOT REACTIVE</p>
</section>

<section class="card card--front" aria-label="Card front">
  <div class="front-band"></div>
  <div class="front-disc"></div>
  <div class="brand">
    <h1 class="brand__name">Steadfast Upkeep<br>Engineering</h1>
    <p class="brand__tag">Keeping your equipment running smoothly</p>
  </div>
  <div class="person">
    <p class="person__name">Dale Harwick</p>
    <p class="person__title">Owner</p>
  </div>
  <ul class="contacts">
    <li><svg viewBox="0 0 24 24"><path d="M6.6 10.8a15 15 0 0 0 6.6 6.6l2.2-2.2c.3-.3.7-.4 1-.2 1.1.4 2.3.6 3.6.6.6 0 1 .4 1 1V20c0 .6-.4 1-1 1A17 17 0 0 1 3 4c0-.6.4-1 1-1h3.5c.6 0 1 .4 1 1 0 1.3.2 2.5.6 3.6.1.3 0 .7-.2 1z"/></svg>5073918246</li>
    <li><svg viewBox="0 0 24 24"><path d="M2 5h20v14H2zm2 2v.5l8 5 8-5V7l-8 5z"/></svg>dale@suevx.com</li>
    <li><svg viewBox="0 0 24 24"><path d="M12 2a10 10 0 1 0 0 20 10 10 0 0 0 0-20zm6.9 6h-3a15 15 0 0 0-1.3-4A8 8 0 0 1 18.9 8zM12 4c.8 1.2 1.5 2.5 1.9 4h-3.8c.4-1.5 1.1-2.8 1.9-4zM4.3 14a8 8 0 0 1 0-4h3.4a16 16 0 0 0 0 4zm.8 2h3a15 15 0 0 0 1.3 4A8 8 0 0 1 5.1 16zm3-8h-3a8 8 0 0 1 4.3-4 15 15 0 0 0-1.3 4zM12 20c-.8-1.2-1.5-2.5-1.9-4h3.8c-.4 1.5-1.1 2.8-1.9 4zm2.3-6H9.7a14 14 0 0 1 0-4h4.6a14 14 0 0 1 0 4zm.3 6a15 15 0 0 0 1.3-4h3a8 8 0 0 1-4.3 4zm1.7-6a16 16 0 0 0 0-4h3.4a8 8 0 0 1 0 4z"/></svg>suevx.com</li>
  </ul>
</section>

</body>
</html>
```